Bref créative
Business Cards and Stationary for Real Estate Firm
Maple Crest Realty Group
Professional
Dennis R. Holloway
Broker/Owner
4782 Lantern Hill Rd
Suite 308
Petaluma, CA 95862
dholloway@brightharborfirm.com
www.maplecrestrealtygroup.net
DRE # 02947716
There should be a place for a photo of the agent on the front of the card, but can work fine if the agent does not put their photo on it. These card designs will be used for multiple agents, I assume the name, phone numbers, email address, etc can be changed for each agent. The AI files and any others that may be needed are in the uploaded zip file.
The back of the card may be a tag line or some other kind of message.
Files in black and white, and with color.

```html
<!DOCTYPE html>
<html lang="en">
<head>
<meta charset="utf-8">
<title>Maple Crest Realty Group – Business Card</title>
<link href="https://fonts.googleapis.com/css2?family=Cinzel:wght@400;600&family=Lato:wght@400;700&display=swap" rel="stylesheet">
<style>
  :root{
    --page-bg:#e9e9ea;
    --brand-red:#d1222b;
    --brand-red-dark:#9e1118;
    --text-gray:#4a4a4a;
    --muted-gray:#777;
    --card-white:#ffffff;
    --back-light:#b9babc;
    --back-dark:#7d7e81;
    --back-text:#ffffff;
  }
  *{box-sizing:border-box;margin:0;padding:0}
  html,body{width:1200px;height:720px;overflow:hidden}
  body{background:var(--page-bg);font-family:"Lato",Arial,sans-serif;position:relative}

  .card{position:absolute;top:205px;width:540px;height:309px;border-radius:14px;overflow:hidden;
        box-shadow:0 10px 26px rgba(0,0,0,.18)}

  /* back side */
  .card-back{left:40px;background:linear-gradient(160deg,var(--back-light) 0%,var(--back-dark) 100%);
             color:var(--back-text);text-align:center}
  .back-brand{position:absolute;top:92px;left:0;right:0;font-family:"Cinzel",Georgia,serif;
              font-weight:400;font-size:34px;letter-spacing:1px;line-height:1.15}
  .back-url{position:absolute;top:196px;left:0;right:0;font-family:"Cinzel",Georgia,serif;
            font-size:13px;letter-spacing:1.5px;text-transform:uppercase}

  /* front side */
  .card-front{left:620px;background:var(--card-white)}
  .front-band{position:absolute;left:0;right:0;bottom:0;height:26px;
              background:linear-gradient(180deg,var(--brand-red) 0%,var(--brand-red-dark) 100%)}
  .front-brand{position:absolute;left:34px;top:118px;width:230px;display:flex;align-items:center;gap:10px}
  .brand-mark{flex:none;width:14px;height:14px;background:var(--brand-red)}
  .brand-name{font-family:"Cinzel",Georgia,serif;font-weight:600;font-size:24px;line-height:1.15;color:var(--brand-red)}

  .contact{position:absolute;left:292px;top:30px;width:230px;color:var(--text-gray);font-size:11.5px;line-height:1.55}
  .agent-name{font-family:"Cinzel",Georgia,serif;font-weight:600;font-size:18px;color:var(--brand-red);line-height:1.2}
  .agent-title{font-family:"Cinzel",Georgia,serif;font-size:11px;letter-spacing:1px;color:var(--muted-gray);
               text-transform:uppercase;margin-bottom:12px}
  .contact-line{display:flex;align-items:center;gap:6px}
  .contact-line svg{width:11px;height:11px;flex:none;fill:var(--brand-red)}
  .address{margin-bottom:6px}
  .email{font-size:10.5px}

  .badge{position:absolute;right:22px;bottom:38px;width:18px;height:18px;background:var(--brand-red)}
</style>
</head>
<body>

<section class="card card-back" aria-label="Card back">
  <div class="back-brand">Maple Crest<br>Realty Group</div>
  <div class="back-url">www.maplecrestrealtygroup.net</div>
</section>

<section class="card card-front" aria-label="Card front">
  <div class="front-brand">
    <span class="brand-mark"></span>
    <span class="brand-name">Maple Crest Realty Group</span>
  </div>

  <div class="contact">
    <div class="agent-name">Dennis R. Holloway</div>
    <div class="agent-title">Broker/Owner</div>
    <div class="address">
      DRE # 02947716<br>
      4782 Lantern Hill Rd<br>
      Suite 308, Petaluma, CA 95862
    </div>
    <div class="contact-line">
      <svg viewBox="0 0 24 24"><path d="M6.6 10.8a15.1 15.1 0 0 0 6.6 6.6l2.2-2.2a1 1 0 0 1 1-.25 11.4 11.4 0 0 0 3.6.57 1 1 0 0 1 1 1V20a1 1 0 0 1-1 1A17 17 0 0 1 3 4a1 1 0 0 1 1-1h3.5a1 1 0 0 1 1 1c0 1.25.2 2.45.57 3.57a1 1 0 0 1-.25 1z"/></svg>
      (415) 555-0142
    </div>
    <div class="contact-line">
      <svg viewBox="0 0 24 24"><path d="M7 1h10a2 2 0 0 1 2 2v18a2 2 0 0 1-2 2H7a2 2 0 0 1-2-2V3a2 2 0 0 1 2-2zm0 4v13h10V5z"/></svg>
      (707) 555-0178
    </div>
    <div class="contact-line">
      <svg viewBox="0 0 24 24"><path d="M6 2h10v5H6zM4 8h16a2 2 0 0 1 2 2v8h-4v4H6v-4H2v-8a2 2 0 0 1 2-2zm4 8v4h8v-4z"/></svg>
      (888) 555-0193
    </div>
    <div class="contact-line email">
      <svg viewBox="0 0 24 24"><path d="M2 5h20v14H2zm2 2v.5l8 5 8-5V7zm0 2.8V17h16V9.8l-8 5z"/></svg>
      dholloway@brightharborfirm.com
    </div>
  </div>

  <span class="badge" aria-hidden="true"></span>
  <div class="front-band"></div>
</section>

</body>
</html>
```